Lantern Business Cards

Need business cards for my employees at my restaurant.

Needs to include:
Our Logo
Lantern Bowls & Brews
Name: Nora Pettigrew
Title : Owner
Address: 487 Mirella Ave. Cedar Hollow, NV 86519
Web: www.lanternkestrel.com
Phone: 555-201-0147
Cell: 555-201-0192
Email: info@lanternkestrel.com

```html
<!DOCTYPE html>
<html lang="en">
<head>
<meta charset="utf-8">
<title>Lantern Bowls &amp; Brews — Business Card</title>
<link href="https://fonts.googleapis.com/css2?family=Open+Sans:wght@400;600;800&family=Montserrat:wght@500&display=swap" rel="stylesheet">
<style>
  :root {
    --brand-red: #9b2230;
    --charcoal: #1f1f20;
    --ink: #3a3a3a;
    --paper: #ffffff;
    --backdrop: #2a2a2b;
    --muted-line: #ffffff;
  }
  * { box-sizing: border-box; margin: 0; padding: 0; }
  html, body { width: 1200px; height: 985px; overflow: hidden; }
  body {
    background: var(--backdrop);
    font-family: "Open Sans", Arial, sans-serif;
    position: relative;
  }
  .card {
    position: absolute;
    left: 250px;
    width: 700px;
    height: 400px;
    overflow: hidden;
    box-shadow: 0 14px 30px rgba(0,0,0,.45);
  }
  /* back side */
  .card--back { top: 55px; background: var(--charcoal); }
  .card__pattern {
    position: absolute; inset: 0;
    background: radial-gradient(circle at 50% 45%, #2b2b2c 0%, #1b1b1c 75%);
  }
  .back__brand {
    position: absolute; left: 0; right: 0; top: 150px;
    text-align: center;
  }
  .wordmark {
    font-family: "Open Sans", Arial, sans-serif;
    font-weight: 800;
    color: var(--brand-red);
    text-transform: uppercase;
    letter-spacing: 2px;
    line-height: 1;
  }
  .back__brand .wordmark { font-size: 84px; }
  .tagline {
    display: flex; align-items: center; justify-content: center; gap: 14px;
    font-family: "Montserrat", Arial, sans-serif;
    font-weight: 500;
    text-transform: uppercase;
    letter-spacing: 2px;
  }
  .tagline::before, .tagline::after {
    content: ""; height: 2px; background: currentColor;
  }
  .back__brand .tagline { color: var(--muted-line); font-size: 15px; margin-top: 14px; }
  .back__brand .tagline::before, .back__brand .tagline::after { width: 90px; }

  /* front side */
  .card--front { top: 530px; background: var(--paper); }
  .front__info { position: absolute; left: 40px; top: 36px; width: 340px; }
  .front__info .wordmark { font-size: 46px; }
  .front__info .tagline { color: var(--ink); font-size: 9px; margin-top: 6px; justify-content: flex-start; }
  .front__info .tagline::before, .front__info .tagline::after { width: 48px; }
  .person__name {
    margin-top: 30px;
    font-weight: 800; font-size: 24px; letter-spacing: 1px;
    color: var(--brand-red); text-transform: uppercase;
  }
  .person__title { font-size: 17px; color: var(--ink); }
  .rule { width: 28px; height: 2px; background: var(--brand-red); margin: 12px 0 10px; }
  .address { font-size: 17px; color: var(--ink); line-height: 1.3; }
  .contacts { list-style: none; font-size: 17px; color: var(--ink); line-height: 1.4; }
  .contacts li { display: flex; align-items: center; gap: 8px; }
  .contacts svg { width: 13px; height: 13px; fill: var(--brand-red); flex: none; }
  .front__art {
    position: absolute; right: 0; top: 0; width: 330px; height: 100%;
    background: linear-gradient(135deg, #f2f2f2 0%, #2a2a2b 55%, var(--brand-red) 100%);
  }
</style>
</head>
<body>
  <section class="card card--back" aria-label="Card back">
    <div class="card__pattern" role="img" aria-label="Subtle repeating brand pattern on dark stock"></div>
    <div class="back__brand">
      <div class="wordmark">Lantern</div>
      <div class="tagline">Bowls and Brews</div>
    </div>
  </section>

  <section class="card card--front" aria-label="Card front">
    <div class="front__info">
      <div class="wordmark">Lantern</div>
      <div class="tagline">Bowls and Brews</div>
      <div class="person__name">Nora Pettigrew</div>
      <div class="person__title">Owner</div>
      <div class="rule"></div>
      <p class="address">487 Mirella Ave.<br>Cedar Hollow, NV 86519</p>
      <div class="rule"></div>
      <ul class="contacts">
        <li><svg viewBox="0 0 24 24"><path d="M6.6 10.8a15 15 0 0 0 6.6 6.6l2.2-2.2a1 1 0 0 1 1-.25 11.4 11.4 0 0 0 3.6.6 1 1 0 0 1 1 1V20a1 1 0 0 1-1 1A17 17 0 0 1 3 4a1 1 0 0 1 1-1h3.5a1 1 0 0 1 1 1c0 1.25.2 2.45.6 3.6a1 1 0 0 1-.25 1z"/></svg>555-201-0147</li>
        <li><svg viewBox="0 0 24 24"><path d="M7 1h10a2 2 0 0 1 2 2v18a2 2 0 0 1-2 2H7a2 2 0 0 1-2-2V3a2 2 0 0 1 2-2zm0 3v14h10V4z"/></svg>555-201-0192</li>
        <li><svg viewBox="0 0 24 24"><path d="M2 5h20v14H2zm2 2v.5l8 5 8-5V7z"/></svg>info@lanternkestrel.com</li>
        <li><svg viewBox="0 0 24 24"><circle cx="12" cy="12" r="10"/></svg>www.lanternkestrel.com</li>
      </ul>
    </div>
    <div class="front__art" role="img" aria-label="Large brand illustration in red, charcoal and white"></div>
  </section>
</body>
</html>
```